Need Catering Menu designed - design that we want is attached

Hi,
We need a new catering menu designed for our cafe.
I have attached our coffee menu, we would like it to follow the same kind of layout.
It needs to be A4, and can be double sided.
I have attached a word doc of our catering menu, so this is what needs to be on the catering menu you produce.
Also, our contact details need to be on both sides of the menu:
Visit us instore to discuss catering options, or call 0438 672 914 or email martha@velbrisco.com.au
I have also attached our new logo which I'd like incorporated into the menu
Doctors/Nurses
Hospital staff
University Students
Catering

```html
<!DOCTYPE html>
<html lang="en">
<head>
<meta charset="utf-8">
<title>Bedside Brew – Catering Menu</title>
<link rel="stylesheet" href="https://fonts.googleapis.com/css2?family=Cutive&family=Oswald:wght@500&display=swap">
<style>
  :root {
    --board: #a06b5c;
    --board-light: #b07a6a;
    --board-dark: #8e5c4f;
    --chalk: #ffffff;
    --logo-dark: #3a2424;
    --page: #ffffff;
  }
  * { margin: 0; padding: 0; box-sizing: border-box; }
  html, body { width: 1200px; height: 935px; overflow: hidden; background: var(--page); }
  .menu-sheet {
    position: relative;
    width: 1200px; height: 848px;
    background: radial-gradient(ellipse at 45% 40%, var(--board-light) 0%, var(--board) 55%, var(--board-dark) 100%);
    color: var(--chalk);
    font-family: "Cutive", "Courier New", serif;
  }
  .brand {
    position: absolute; left: 523px; top: 29px;
    width: 128px; height: 128px; border-radius: 50%;
    background: var(--logo-dark);
    display: flex; align-items: center; justify-content: center;
    font-size: 14px; letter-spacing: 1px; text-align: center; line-height: 1.3;
  }
  .menu-title {
    position: absolute; left: 0; right: 0; top: 164px;
    text-align: center; font-size: 25px; letter-spacing: 1px; font-weight: 400;
  }
  .menu-box {
    position: absolute; border: 2px solid var(--chalk);
  }
  .menu-box--breakfast { left: 76px; top: 254px; width: 481px; height: 508px; }
  .menu-box--tea { left: 606px; top: 254px; width: 524px; height: 362px; }
  .menu-box--notes { left: 606px; top: 638px; width: 524px; height: 124px; }
  .ribbon {
    position: absolute; top: 222px; height: 62px;
  }
  .ribbon--breakfast { left: 155px; width: 322px; }
  .ribbon--tea { left: 649px; width: 436px; }
  .ribbon svg { position: absolute; inset: 0; width: 100%; height: 100%; }
  .ribbon h2 {
    position: relative; height: 100%;
    display: flex; align-items: center; justify-content: center;
    font-family: "Oswald", "Arial Narrow", sans-serif; font-weight: 500;
    font-size: 29px; letter-spacing: 0.5px; text-transform: uppercase;
  }
  .item-list { position: absolute; list-style: none; }
  .menu-box--breakfast .item-list { left: 40px; right: 44px; top: 50px; }
  .menu-box--tea .item-list { left: 42px; right: 56px; top: 51px; }
  .item-list li {
    display: flex; align-items: baseline;
    height: 31px; font-size: 17px;
  }
  .item-list .leader {
    flex: 1; margin: 0 3px;
    border-bottom: 2px dotted var(--chalk);
    transform: translateY(-4px);
  }
  .notes { position: absolute; left: 30px; top: 26px; right: 30px; list-style: none; font-size: 13.5px; line-height: 1.45; }
  .notes li { position: relative; padding-left: 14px; margin-bottom: 16px; }
  .notes li::before { content: "*"; position: absolute; left: 0; top: 0; }
  .contact {
    position: absolute; left: 0; right: 0; top: 784px;
    text-align: center; font-size: 17px;
  }
</style>
</head>
<body>
<main class="menu-sheet">
  <div class="brand">BEDSIDE<br>BREW</div>
  <h1 class="menu-title">Catering Menu</h1>

  <section class="menu-box menu-box--breakfast">
    <ul class="item-list">
      <li>Fruit Platter<span class="leader"></span>$15</li>
      <li>Bacon Egg and Cheese Roll<span class="leader"></span>$6.5</li>
      <li>Vegetarian Brekky Wrap<span class="leader"></span>$6.5</li>
      <li>Ham and Cheese Croissant<span class="leader"></span>$6</li>
      <li>Cheese and Tomato Croissant<span class="leader"></span>$5.5</li>
      <li>Ham and Cheese French Toast<span class="leader"></span>$6.5</li>
      <li>Assorted Yoghurts<span class="leader"></span>$5.5</li>
      <li>Bircher Muesli<span class="leader"></span>$5.5</li>
      <li>Chia Pudding<span class="leader"></span>$5.5</li>
      <li>Granola and Yoghurt<span class="leader"></span>$5.5</li>
      <li>Muffin<span class="leader"></span>$4.5</li>
      <li>Mini Muffin<span class="leader"></span>$2.5</li>
      <li>Juice<span class="leader"></span>$8</li>
    </ul>
  </section>
  <div class="ribbon ribbon--breakfast">
    <svg viewBox="0 0 322 62" preserveAspectRatio="none" aria-hidden="true">
      <polygon points="1,6 321,6 305,31 321,56 1,56 17,31" fill="var(--board)" stroke="var(--chalk)" stroke-width="2"/>
      <polygon points="24,1 298,1 298,61 24,61" fill="var(--board)" stroke="var(--chalk)" stroke-width="2"/>
    </svg>
    <h2>Breakfast</h2>
  </div>

  <section class="menu-box menu-box--tea">
    <ul class="item-list">
      <li>Fruit Platter<span class="leader"></span>$15</li>
      <li>Muffin<span class="leader"></span>$4.5</li>
      <li>Mini Muffin<span class="leader"></span>$2.5</li>
      <li>Assorted Slices<span class="leader"></span>$4</li>
      <li>Assorted Cookies from<span class="leader"></span>$3</li>
      <li>Assorted Yoghurts<span class="leader"></span>$5.5</li>
      <li>Chia Pudding<span class="leader"></span>$5.5</li>
      <li>Banana Bread<span class="leader"></span>$4.5</li>
      <li>Juice<span class="leader"></span>$8</li>
    </ul>
  </section>
  <div class="ribbon ribbon--tea">
    <svg viewBox="0 0 436 62" preserveAspectRatio="none" aria-hidden="true">
      <polygon points="1,6 435,6 419,31 435,56 1,56 17,31" fill="var(--board)" stroke="var(--chalk)" stroke-width="2"/>
      <polygon points="24,1 412,1 412,61 24,61" fill="var(--board)" stroke="var(--chalk)" stroke-width="2"/>
    </svg>
    <h2>Morning and Afternoon Tea</h2>
  </div>

  <section class="menu-box menu-box--notes">
    <ul class="notes">
      <li>Cups/Plates/Serviettes can be provided at a charge of<br>$1 per person</li>
      <li>Barista made coffee available</li>
    </ul>
  </section>

  <p class="contact">Visit us instore to discuss catering options, or call 0438 672 914 or email martha@velbrisco.com.au</p>
</main>
</body>
</html>
```